Design some Business Cards for Professional Cleaning company

Double sided card/ Standard card (I believe 3.5" x 2")
Unique
I have a logo already (Which is awesome)
Contact info: Marta Quill
martaquill@thebrightcornercleaning.example
(404) 555-0182
thebrightcornercleaning.example
Servicing Atlanta and Surrounding Areas
List of my services somehow without it looking cluttered
-Commercial/ New Construction clean up
-Residential/ rental property turn over
-move ins/move outs (Tenant)
-Pre/Post Event Clean Up
-Office Cleaning
-Restaurants and more!
I am open and versatile and very appreciative

```html
<!DOCTYPE html>
<html lang="en">
<head>
<meta charset="utf-8">
<title>The Bright Corner – Business Cards</title>
<link href="https://fonts.googleapis.com/css2?family=Source+Sans+3:wght@400;600;700&display=swap" rel="stylesheet">
<style>
  :root {
    --stage: #cacacc;
    --navy: #0b3a6f;
    --navy-deep: #07305e;
    --sky: #4cc0e6;
    --sky-bright: #18b7ee;
    --aqua: #5bc1dd;
    --teal-soft: #7fcfd9;
    --ice: #9fdcec;
    --white: #ffffff;
    --brand-blue: #1f8fd0;
  }
  * { box-sizing: border-box; margin: 0; padding: 0; }
  html, body { width: 1200px; height: 1200px; overflow: hidden; }
  body {
    background: var(--stage);
    font-family: "Source Sans 3", "Helvetica Neue", Arial, sans-serif;
    position: relative;
  }
  .card {
    position: absolute;
    left: 186px;
    width: 828px;
    height: 510px;
    border-radius: 22px;
    overflow: hidden;
    background: var(--navy);
  }
  .card--front { top: 42px; }
  .card--back { top: 592px; }

  /* decorative band areas, kept as soft colour fields */
  .band-field {
    position: absolute;
    left: 0;
    background: linear-gradient(170deg, var(--navy) 0%, var(--aqua) 35%, var(--sky-bright) 65%, var(--navy) 100%);
    opacity: 0.9;
  }
  .card--front .band-field { top: 300px; width: 828px; height: 210px; }
  .card--back .band-field { top: 262px; width: 414px; height: 248px; }

  /* brand lockup */
  .brand {
    display: flex;
    flex-direction: column;
    align-items: center;
    gap: 8px;
    color: var(--brand-blue);
    font-weight: 700;
    line-height: 1;
  }
  .brand__dot {
    width: 58px; height: 58px;
    border-radius: 50%;
    background: var(--brand-blue);
  }
  .brand__name { font-size: 22px; letter-spacing: 0.2px; }

  /* front */
  .front__tab {
    position: absolute;
    left: 0; top: 75px;
    width: 410px; height: 142px;
    background: var(--aqua);
    border-radius: 0 18px 18px 0;
  }
  .front__tab .brand {
    position: absolute;
    left: 110px; top: 16px;
    width: 200px;
    color: var(--navy-deep);
    gap: 10px;
  }
  .front__tab .brand__dot { width: 62px; height: 62px; background: var(--navy-deep); }
  .front__tab .brand__name { font-size: 20px; }
  .front__tagline {
    position: absolute;
    right: 0; top: 249px;
    width: 344px; height: 68px;
    background: var(--white);
    border-radius: 16px 0 0 16px;
    display: flex; align-items: center; justify-content: center;
    color: var(--navy);
    font-size: 24px;
  }

  /* back */
  .back__panel {
    position: absolute; right: 0; top: 0;
    width: 414px; height: 100%;
    background: var(--white);
  }
  .back__brand {
    position: absolute; left: 0; top: 40px; width: 414px;
  }
  .back__brand .brand__dot { width: 76px; height: 76px; }
  .pill {
    position: absolute;
    left: 46px;
    width: 321px;
    border-radius: 20px;
    display: flex; align-items: center;
    padding-left: 10px;
  }
  .pill__icon { width: 48px; height: 48px; flex: none; }
  .pill__text { flex: 1; text-align: center; padding-right: 10px; white-space: nowrap; }
  .pill--phone { top: 15px; height: 68px; background: var(--navy); color: var(--sky); font-size: 17px; }
  .pill--email { top: 98px; height: 64px; background: var(--teal-soft); color: var(--white); font-size: 12px; }
  .pill--web { top: 177px; height: 68px; background: var(--sky); color: var(--navy); font-size: 16px; }
  .services {
    position: absolute;
    left: 56px; top: 278px;
    width: 312px; height: 218px;
    background: var(--navy);
    border-radius: 34px;
    color: var(--sky);
    text-align: center;
    font-size: 14px;
    line-height: 1.25;
    padding-top: 30px;
  }
  .services__area { margin-bottom: 16px; }
  .services__list { list-style: none; }
</style>
</head>
<body>

<section class="card card--front" aria-label="Card front">
  <div class="band-field" role="img" aria-label="Flowing blue wave decoration across the lower card"></div>

  <div class="front__tab">
    <div class="brand">
      <span class="brand__dot"></span>
      <span class="brand__name">The Bright Corner</span>
    </div>
  </div>
  <div class="front__tagline">Professional cleaning services</div>
</section>

<section class="card card--back" aria-label="Card back">
  <div class="band-field" role="img" aria-label="Flowing blue wave decoration across the lower left"></div>

  <div class="brand back__brand">
    <span class="brand__dot"></span>
    <span class="brand__name">The Bright Corner</span>
  </div>

  <div class="back__panel">
    <div class="pill pill--phone">
      <svg class="pill__icon" viewBox="0 0 48 48" aria-hidden="true">
        <path d="M14 10c3-2 5 0 6 3l2 5c1 2 0 3-2 4l-2 1c2 4 5 7 9 9l1-2c1-2 2-3 4-2l5 2c3 1 5 3 3 6-2 4-6 5-10 3-8-4-14-10-18-18-2-4-1-8 2-11z" fill="#4cc0e6"/>
      </svg>
      <span class="pill__text">(404) 555-0182</span>
    </div>
    <div class="pill pill--email">
      <svg class="pill__icon" viewBox="0 0 48 48" aria-hidden="true">
        <rect x="6" y="12" width="36" height="24" fill="#ffffff" stroke="#0b3a6f" stroke-width="1.5"/>
        <path d="M6 12 L24 27 L42 12 M6 36 L19 23 M42 36 L29 23" fill="none" stroke="#0b3a6f" stroke-width="1.5"/>
      </svg>
      <span class="pill__text">martaquill@thebrightcornercleaning.example</span>
    </div>
    <div class="pill pill--web">
      <svg class="pill__icon" viewBox="0 0 48 48" aria-hidden="true">
        <g fill="none" stroke="#0b3a6f" stroke-width="2.5">
          <circle cx="24" cy="24" r="15"/>
          <ellipse cx="24" cy="24" rx="6.5" ry="15"/>
          <path d="M9 24h30M12 16h24M12 32h24"/>
        </g>
      </svg>
      <span class="pill__text">thebrightcornercleaning.example</span>
    </div>
    <div class="services">
      <p class="services__area">Servicing Atlanta and Surrounding Areas</p>
      <ul class="services__list">
        <li>-Commercial/ New Construction clean up</li>
        <li>-Residential/ rental property turn over</li>
        <li>-move ins/move outs (Tenant)</li>
        <li>-Pre/Post Event Clean Up</li>
        <li>-Office Cleaning</li>
        <li>-Restaurants and more!</li>
      </ul>
    </div>
  </div>
</section>

</body>
</html>
```